1 page marketing brochure for subcontractor services for Florida's Petroleum Contamination cleanup

I need a marketing brochure that can be emailed to potential clients to offer our comprehensive service capabilities to Agency Term Contractors in the Coastal Bureau of Habitat Stewardship's (CBHS) Fuel Recovery Initiative. We offer turnkey support from project management, monitoring, reporting, soil and groundwater assessment, remediation system engineering, design, construction, and system rental. We would like to see designs that use the green and goldish colors in our logo. I have attached the icon from our logo and an amateur in-house created design with some key points that are important to us. The icons used as bullet points can change. I've added examples of industry correct drilling icons. I also added a second picture of a system trailer in use. We are open to different Fonts and are open to assistance with copy refinement. This single page flyer is intended only for digital use (email/website) at this time.
Updates

Target Market(s)

Agency Term contractors in Coastal Bureau of Habitat Stewardship Fuel Recovery Initiative

Industry/Entity Type

Petroleum cleanup in Florida

Requirements
Should not have
• Don't show the Brimor name in the photo. See attached examples of industry appropriate drilling icons

```html
<!DOCTYPE html>
<html lang="en">
<head>
<meta charset="utf-8">
<title>Meridian – Your Subcontracting Partner</title>
<link rel="stylesheet" href="https://fonts.googleapis.com/css2?family=Montserrat:ital,wght@0,400;0,500;0,600;0,700;0,800;1,500;1,600;1,800&display=swap">
<style>
  :root {
    --backdrop: #d9d9d9;
    --green: #1f6b3b;
    --green-dark: #17552e;
    --gold: #b39234;
    --gold-dark: #8a6f22;
    --photo-top: #5b5f63;
    --photo-bottom: #3a3c3e;
    --white: #ffffff;
    --ink: #161616;
    --ink-soft: #3a3a3a;
    --sans: "Montserrat", Arial, sans-serif;
  }
  * { box-sizing: border-box; margin: 0; padding: 0; }
  html, body { width: 1200px; height: 1200px; overflow: hidden; }
  body { background: var(--backdrop); font-family: var(--sans); position: relative; }

  .flyer {
    position: absolute; left: 212px; top: 52px;
    width: 597px; height: 843px;
    transform: scale(1.3); transform-origin: top left;
    background: var(--green); overflow: hidden; color: var(--white);
  }

  .hero-photo {
    position: absolute; left: 0; top: 0; width: 597px; height: 400px;
    background: linear-gradient(180deg, var(--photo-top) 0%, #4a4d50 45%, var(--photo-bottom) 100%);
  }
  .hero-shape { position: absolute; left: 0; top: 0; width: 597px; height: 843px; }

  .hero-title {
    position: absolute; left: 39px; top: 60px;
    font-weight: 800; font-style: italic; font-size: 31px; line-height: 34px;
    letter-spacing: 0.5px; text-transform: uppercase;
  }
  .hero-subtitle {
    position: absolute; left: 39px; top: 182px;
    font-weight: 500; font-size: 15.5px; line-height: 21px; text-transform: uppercase;
  }
  .hero-tagline {
    position: absolute; left: 39px; top: 238px;
    font-weight: 600; font-style: italic; font-size: 15.5px;
  }

  .brand-mark {
    position: absolute; left: 410px; top: 122px; width: 150px; height: 150px;
    display: flex; align-items: center; justify-content: center;
  }
  .brand-mark .square {
    position: absolute; inset: 18px; background: var(--green);
    transform: rotate(6deg);
  }
  .brand-mark .name {
    position: relative; font-weight: 800; font-size: 16px; color: var(--white); letter-spacing: 1px;
  }

  .ribbon { position: absolute; left: 404px; top: 350px; width: 172px; height: 205px; }
  .ribbon-label {
    position: absolute; left: 422px; top: 392px; width: 152px; text-align: center;
  }
  .ribbon-label .number { display: block; font-weight: 800; font-size: 78px; line-height: 80px; }
  .ribbon-label .unit { display: block; font-weight: 500; font-style: italic; font-size: 25px; margin-top: -6px; text-align: right; padding-right: 6px; }

  .intro { position: absolute; left: 39px; top: 400px; width: 375px; }
  .intro h2 { font-weight: 700; font-size: 12.5px; margin-bottom: 1px; }
  .intro p { font-weight: 400; font-size: 10.4px; line-height: 13.5px; margin-bottom: 12px; color: #eef3ef; }

  .services {
    position: absolute; left: 0; top: 562px; width: 484px; height: 100px;
    background: var(--white); border-radius: 0 22px 22px 0;
    box-shadow: 0 3px 8px rgba(0,0,0,0.35);
    padding: 10px 0 0 39px; color: var(--ink);
  }
  .services h2 { font-weight: 700; font-size: 16px; margin-bottom: 6px; }
  .services ul { list-style: none; display: grid; grid-template-columns: 204px 210px; row-gap: 5px; }
  .services li { font-size: 10.5px; color: var(--ink-soft); }

  .checklist li::before { content: "✔"; font-size: 8px; margin-right: 5px; }

  .why { position: absolute; left: 39px; top: 694px; }
  .why h2, .mission h2 { font-weight: 700; font-size: 12.5px; margin-bottom: 14px; letter-spacing: 0.3px; }
  .why ul { list-style: none; }
  .why li { font-size: 10.5px; margin-bottom: 7px; color: #eef3ef; }

  .mission { position: absolute; left: 338px; top: 694px; }
  .mission p { font-size: 10.5px; line-height: 14px; color: #eef3ef; }

  .contact {
    position: absolute; left: 310px; top: 762px; width: 287px; height: 58px;
    background: var(--gold); padding: 6px 0 0 27px; list-style: none;
  }
  .contact li { display: flex; align-items: center; font-size: 10.5px; line-height: 15px; }
  .contact svg { width: 7px; height: 7px; margin-right: 12px; fill: var(--white); }
</style>
</head>
<body>
  <article class="flyer">
    <div class="hero-photo" role="img" aria-label="Drilling rig and crew working beside traffic cones at a fuel station forecourt"></div>

    <svg class="hero-shape" viewBox="0 0 597 843" aria-hidden="true">
      <polygon points="0,284 597,384 597,843 0,843" fill="var(--green)"/>
      <line x1="0" y1="284" x2="597" y2="384" stroke="var(--white)" stroke-width="3"/>
    </svg>

    <h1 class="hero-title">Your<br>Subcontracting<br>Partner</h1>
    <p class="hero-subtitle">For ATCs in Florida's Fuel<br>Recovery Initiative</p>
    <p class="hero-tagline">Offering Turnkey Project Support</p>

    <div class="brand-mark">
      <span class="square"></span>
      <span class="name">MERIDIAN</span>
    </div>

    <svg class="ribbon" viewBox="0 0 172 205" aria-hidden="true">
      <polygon points="0,2 18,2 18,24" fill="var(--gold-dark)"/>
      <polygon points="18,2 172,2 172,160 95,202 18,160" fill="var(--gold)"/>
    </svg>
    <div class="ribbon-label">
      <span class="number">40</span>
      <span class="unit">Years</span>
    </div>

    <section class="intro">
      <h2>Partner with Experience you can Trust</h2>
      <p>With 40 years of service to CBHS and the Fuel Recovery Initiative, Meridian offers unmatched expertise in all phases of site assessment and remediation.</p>
      <p>For the new contract period, Meridian will not be an ATC and instead will be providing support to ATC firms by subcontracting our services to others. Meridian remains in good standing with CBHS and will continue to offer our high quality comprehensive service capabilities to ATCs across the state.</p>
    </section>

    <section class="services">
      <h2>OUR SERVICES</h2>
      <ul class="checklist">
        <li>Project Management Support</li>
        <li>Soil &amp; Groundwater Assessment</li>
        <li>System Engineering &amp; Design</li>
        <li>Drilling &amp; Well Installation</li>
        <li>System Construction, Rental &amp; O&amp;M</li>
        <li>Monitoring &amp; Reporting</li>
      </ul>
    </section>

    <section class="why">
      <h2>WHY CHOOSE MERIDIAN?</h2>
      <ul class="checklist">
        <li>Comprehensive Capabilities</li>
        <li>Recognized Top Performer</li>
        <li>Deep Program Knowledge</li>
        <li>Experienced In-house Personnel</li>
      </ul>
    </section>

    <section class="mission">
      <h2>YOUR SUCCESS IS OUR MISSION</h2>
      <p>Together, we restore Florida's environment<br>safely · efficiently · effectively</p>
    </section>

    <ul class="contact">
      <li><svg viewBox="0 0 10 10"><path d="M2 0.5 L3.8 2.6 L2.9 3.7 Q4 6 6.3 7.1 L7.4 6.2 L9.5 8 L8.4 9.5 Q3 9 0.5 1.6 Z"/></svg>555-014-2290</li>
      <li><svg viewBox="0 0 10 10"><path d="M0 1.5 H10 V8.5 H0 Z"/></svg>hello@meridianfieldworks.com</li>
      <li><svg viewBox="0 0 10 10"><circle cx="5" cy="5" r="5"/></svg>www.meridianfieldworks.com</li>
    </ul>
  </article>
</body>
</html>
```